Al Qarmani our website www.klorvin.com

We need a Web Design for a new company called 'KLORVIN'. We develop innovative uPhone applications for consumers. Our initial product is PennyWise - an application that helps people manage their budgets and save money. We would like to see designs that use the color green. The final design should communicate financial safety and growth”.

Target Market(s)

technology and Electrics

Number of Pages Required

1 page

Requirements
Must have
• And work for pomelo and robotix
• To working min 2 languages Arabic and English
Nice to have
Should not have

```html
<!DOCTYPE html>
<html lang="en">
<head>
<meta charset="utf-8">
<title>KLORVIN — Innovative uPhone Applications</title>
<link href="https://fonts.googleapis.com/css2?family=Raleway:wght@300;400;500;600;700&display=swap" rel="stylesheet">
<style>
:root{
  --green:#3bb54a;
  --green-dark:#2f9c3d;
  --green-soft:#cfeed3;
  --ink:#222;
  --muted:#666;
  --dark:#2f2f2f;
  --hero-a:#1a1416;
  --hero-b:#3a2a2c;
  --light:#f7f7f7;
  --white:#fff;
}
*{box-sizing:border-box;margin:0;padding:0}
html,body{width:1200px;height:3502px;overflow:hidden}
body{position:relative;font-family:'Raleway',sans-serif;color:var(--ink);background:var(--white)}
.abs{position:absolute}
a{color:inherit;text-decoration:none}

/* hero */
.hero{left:0;top:0;width:1200px;height:654px;background:linear-gradient(135deg,var(--hero-b) 0%,var(--hero-a) 45%,#2a1c1e 75%,#120d0e 100%)}
.nav a{position:absolute;top:86px;font-size:11px;font-weight:600;color:var(--white);white-space:nowrap}
.brand{position:absolute;top:74px;left:536px;width:128px;text-align:center;color:var(--white);font-weight:700;font-size:22px;letter-spacing:5px}
.brand small{display:block;font-size:9px;letter-spacing:3px;font-weight:500;margin-top:2px;opacity:.8}
.hero h1{position:absolute;top:226px;left:0;width:1200px;text-align:center;color:var(--white);font-weight:400;font-size:40px;line-height:50px}
.hero p{position:absolute;top:340px;left:400px;width:400px;text-align:center;color:#eee;font-size:13px;line-height:20px}
.btn{display:inline-block;background:var(--green);color:var(--white);font-size:12px;font-weight:600;text-align:center;border-radius:2px;white-space:nowrap}
.hero .btn{position:absolute;left:518px;top:425px;width:160px;height:34px;line-height:34px}

/* about */
.about-title{left:135px;top:766px;font-size:36px;font-weight:400;line-height:44px;color:var(--ink)}
.about-text{left:135px;width:380px;font-size:12.5px;line-height:23px;color:#444}
.social{left:135px;top:1044px;display:flex;gap:28px}
.social span{width:26px;height:26px;border-radius:50%;background:#cfcfcf}
.about-green{left:619px;top:761px;width:462px;height:280px;background:linear-gradient(135deg,var(--green) 0%,#49c65a 100%)}
.about-photo{left:588px;top:789px;width:463px;height:280px;background:linear-gradient(135deg,#d9d2c6 0%,#8a7d6c 45%,#3d3631 100%);border:4px solid var(--white);box-shadow:0 4px 12px rgba(0,0,0,.2)}

/* projects */
.projects{left:0;top:1184px;width:1200px;height:750px;background:linear-gradient(120deg,#4a4a4a 0%,#2c2c2c 50%,#3c3c3c 100%)}
.section-title{width:1200px;left:0;text-align:center;font-size:28px;font-weight:400}
.rule{left:580px;width:40px;height:2px}
.card-phone{position:absolute;background:var(--white);border-radius:14px}
.phone{position:absolute;left:511px;top:1371px;width:196px;height:408px;border-radius:26px;background:#111;padding:8px}
.phone .screen{width:100%;height:100%;border-radius:19px;background:var(--white);display:flex;align-items:center;justify-content:center;text-align:center;color:#888;font-size:18px;line-height:22px}
.phone .notch{position:absolute;left:68px;top:8px;width:60px;height:12px;background:#111;border-radius:0 0 8px 8px}
.dots{left:564px;top:1846px;display:flex;gap:8px}
.dots span{width:10px;height:10px;border-radius:50%;background:#999}
.dots span.on{background:var(--white)}

/* pricing */
.pricing{left:0;top:1966px;width:1200px;height:801px;background:var(--light)}
.sq{position:absolute;background:var(--green-soft)}
.plan{position:absolute;top:2139px;width:376px;height:495px;padding:28px 34px;box-shadow:0 2px 8px rgba(0,0,0,.18)}
.plan h3{font-size:22px;font-weight:500;margin-bottom:44px}
.plan p{width:280px;font-size:12.5px;line-height:20px;margin-bottom:20px}
.plan ul{list-style:none;width:290px}
.plan li{position:relative;padding-left:22px;font-size:12.5px;font-weight:600;line-height:18px;margin-bottom:14px}
.plan li svg{position:absolute;left:0;top:3px}
.plan .btn{position:absolute;left:34px;bottom:37px;width:196px;height:42px;line-height:42px;font-size:13px}
.plan.basic{left:226px;background:var(--dark);color:var(--white)}
.plan.custom{left:621px;background:var(--white);color:var(--ink)}

/* testimonials */
.quote{position:absolute;top:2926px;width:340px;height:180px;background:var(--white);box-shadow:0 1px 6px rgba(0,0,0,.15);padding:18px 20px;overflow:hidden}
.quote .who{display:flex;align-items:center;gap:12px;margin-bottom:10px}
.quote .avatar{width:38px;height:38px;border-radius:50%;background:linear-gradient(135deg,#9cc3e6,#5d8fc0);flex:none}
.quote b{display:block;font-size:11px}
.quote em{font-style:normal;font-size:9px;color:var(--muted)}
.quote p{font-size:9px;line-height:15px;color:#777;font-style:italic}
.quote .mark{position:absolute;right:22px;bottom:14px}

/* contact */
.contact-title{left:89px;top:3292px;font-size:26px;font-weight:400}
.check{position:absolute;top:3380px;display:flex;gap:10px;font-size:12px;line-height:15px}
.check .box{width:14px;height:14px;background:#e5e5e5}
.field{left:364px;top:3369px;width:458px;height:46px;border:1px solid #ccc;background:var(--white);font-size:12px;color:#999;padding:0 24px;line-height:44px}
.contact-photo{left:612px;top:3269px;width:588px;height:182px;background:linear-gradient(135deg,#5ccb6a 0%,var(--green) 60%,var(--green-dark) 100%)}
.send{left:836px;top:3369px;width:184px;height:46px;border:1px solid rgba(255,255,255,.8);color:var(--white);font-size:13px;text-align:center;line-height:44px}
.footer{left:0;top:3451px;width:1200px;height:51px;background:var(--white);border-top:1px solid #eee}
.footer-green{left:612px;top:3451px;width:588px;height:51px;background:var(--green)}
.footer-brand{left:105px;top:3468px;font-weight:700;font-size:16px;letter-spacing:4px}
.footer-nav a{position:absolute;top:3472px;font-size:11px;font-weight:600;color:var(--white);white-space:nowrap}
</style>
</head>
<body>

<section class="hero abs" role="img" aria-label="Dark photo of smartphones lying on a table">
  <nav class="nav">
    <a style="left:292px">What is Klorvin?</a>
    <a style="left:408px">Why Norvale?</a>
    <div class="brand">KLORVIN<small>APPS</small></div>
    <a style="left:737px">How it Works</a>
    <a style="left:842px">Contact us</a>
  </nav>
  <h1>Innovative uPhone Applications<br>for&nbsp; Costumers.</h1>
  <p>Have the best application experience by following professional process made by experts</p>
  <a class="btn">Visit the live version</a>
</section>

<h2 class="abs about-title">Few Words About<br>Company</h2>
<p class="abs about-text" style="top:880px">Lorem ipsum dolor sit amet, consectetuer adipiscing elit. Aenean commodo ligula eget dolor. Aenean massa. Cum sociis natoque penatibus et magnis dis parturient.</p>
<p class="abs about-text" style="top:960px">Lorem ipsum dolor sit amet, consectetuer adipiscing elit. Aenean commodo ligula eget dolor.</p>
<div class="abs social" aria-label="Social links"><span></span><span></span><span></span><span></span></div>
<div class="abs about-green"></div>
<div class="abs about-photo" role="img" aria-label="Photo of a team working at laptops around a table"></div>

<section class="abs projects" role="img" aria-label="Dimmed photo of people in an office"></section>
<h2 class="abs section-title" style="top:1264px;color:var(--white)">Our Created Projects</h2>
<div class="abs rule" style="top:1318px;background:var(--white)"></div>
<div class="card-phone" style="left:259px;top:1417px;width:140px;height:311px"></div>
<div class="card-phone" style="left:801px;top:1417px;width:159px;height:311px"></div>
<div class="card-phone" style="left:366px;top:1398px;width:160px;height:349px"></div>
<div class="card-phone" style="left:692px;top:1398px;width:160px;height:349px"></div>
<div class="phone"><div class="screen">Completed<br>Projects images<br>Here</div><div class="notch"></div></div>
<svg class="abs" style="left:134px;top:1572px" width="30" height="22" viewBox="0 0 30 22"><path d="M28 11H3M12 2 3 11l9 9" fill="none" stroke="#fff" stroke-width="2.5"/></svg>
<svg class="abs" style="left:1034px;top:1572px" width="30" height="22" viewBox="0 0 30 22"><path d="M2 11h25M18 2l9 9-9 9" fill="none" stroke="#888" stroke-width="2.5"/></svg>
<div class="abs dots"><span></span><span></span><span class="on"></span><span></span></div>

<section class="abs pricing"></section>
<h2 class="abs section-title" style="top:2034px">Our Pricing Plans</h2>
<div class="abs rule" style="top:2084px;background:#555"></div>
<div class="sq" style="left:404px;top:2096px;width:18px;height:18px"></div>
<div class="sq" style="left:443px;top:2110px;width:34px;height:26px"></div>
<div class="sq" style="left:186px;top:2320px;width:22px;height:40px"></div>
<div class="sq" style="left:110px;top:2440px;width:12px;height:12px"></div>
<div class="sq" style="left:154px;top:2480px;width:14px;height:14px"></div>
<div class="sq" style="left:1004px;top:2180px;width:14px;height:14px"></div>
<div class="sq" style="left:1004px;top:2250px;width:24px;height:30px"></div>
<div class="sq" style="left:1040px;top:2220px;width:12px;height:12px"></div>
<div class="sq" style="left:746px;top:2644px;width:36px;height:30px"></div>
<div class="sq" style="left:716px;top:2668px;width:16px;height:16px"></div>

<article class="plan basic">
  <h3>Basic App</h3>
  <p>Get prepared for your App before you know all the critical information about the market you're travelling to.</p>
  <ul>
    <li><svg width="12" height="10" viewBox="0 0 12 10"><path d="M1 5l3.5 3.5L11 1" fill="none" stroke="#3bb54a" stroke-width="2"/></svg>Simple Market Research</li>
    <li><svg width="12" height="10" viewBox="0 0 12 10"><path d="M1 5l3.5 3.5L11 1" fill="none" stroke="#3bb54a" stroke-width="2"/></svg>User Experience Wireframes to Feel the App</li>
    <li><svg width="12" height="10" viewBox="0 0 12 10"><path d="M1 5l3.5 3.5L11 1" fill="none" stroke="#3bb54a" stroke-width="2"/></svg>Revisions / Visual design, preparation to launch.</li>
    <li><svg width="12" height="10" viewBox="0 0 12 10"><path d="M1 5l3.5 3.5L11 1" fill="none" stroke="#3bb54a" stroke-width="2"/></svg>Launching, observing results.</li>
  </ul>
  <a class="btn">Order this Plan Now</a>
</article>
<article class="plan custom">
  <h3>Custom App</h3>
  <p>Create unique apps on topics and places that you know best, help people explore and sell them to millions of user around the world.</p>
  <ul>
    <li><svg width="12" height="10" viewBox="0 0 12 10"><path d="M1 5l3.5 3.5L11 1" fill="none" stroke="#3bb54a" stroke-width="2"/></svg>Custom database with professionals.</li>
    <li><svg width="12" height="10" viewBox="0 0 12 10"><path d="M1 5l3.5 3.5L11 1" fill="none" stroke="#3bb54a" stroke-width="2"/></svg>Half year of help with testing, providing feedbacks and etc.</li>
    <li><svg width="12" height="10" viewBox="0 0 12 10"><path d="M1 5l3.5 3.5L11 1" fill="none" stroke="#3bb54a" stroke-width="2"/></svg>We help to increase your Visibility</li>
  </ul>
  <a class="btn">Order this Plan Now</a>
</article>

<h2 class="abs section-title" style="top:2840px">Testimonials</h2>
<div class="abs rule" style="top:2888px;background:#555"></div>
<svg class="abs" style="left:1080px;top:2880px" width="46" height="16" viewBox="0 0 46 16"><path d="M20 8H3M9 2 3 8l6 6" fill="none" stroke="#222" stroke-width="2"/><path d="M26 8h17M37 2l6 6-6 6" fill="none" stroke="#999" stroke-width="2"/></svg>

<article class="quote" style="left:-114px">
  <div class="who"><div class="avatar" role="img" aria-label="Client portrait"></div><div><b>Rami Dalton</b><em>CEO &amp; Owner / Studio</em></div></div>
  <p>Working with this team made our launch smooth. The app feels fast, clean and simple, and our users keep coming back to it every single week.</p>
  <svg class="mark" width="26" height="16" viewBox="0 0 26 16"><path d="M2 2h8v7l-4 6H3l3-6H2zM15 2h8v7l-4 6h-3l3-6h-4z" fill="#3bb54a"/></svg>
</article>
<article class="quote" style="left:247px">
  <div class="who"><div class="avatar" role="img" aria-label="Client portrait"></div><div><b>Rami Dalton</b><em>CEO &amp; Owner / Studio</em></div></div>
  <p>Working with this team made our launch smooth. The app feels fast, clean and simple, and our users keep coming back to it every single week.</p>
  <svg class="mark" width="26" height="16" viewBox="0 0 26 16"><path d="M2 2h8v7l-4 6H3l3-6H2zM15 2h8v7l-4 6h-3l3-6h-4z" fill="#3bb54a"/></svg>
</article>
<article class="quote" style="left:609px;height:220px">
  <div class="who"><div class="avatar" role="img" aria-label="Client portrait"></div><div><b>Rami Dalton</b><em>CEO &amp; Owner / Studio</em></div></div>
  <p>Working with this team made our launch smooth. The app feels fast, clean and simple, and our users keep coming back to it every single week.</p>
  <svg class="mark" width="26" height="16" viewBox="0 0 26 16"><path d="M2 2h8v7l-4 6H3l3-6H2zM15 2h8v7l-4 6h-3l3-6h-4z" fill="#3bb54a"/></svg>
</article>
<article class="quote" style="left:969px">
  <div class="who"><div class="avatar" role="img" aria-label="Client portrait"></div><div><b>Rami Dalton</b><em>CEO &amp; Owner / Studio</em></div></div>
  <p>Working with this team made our launch smooth. The app feels fast, clean and simple, and our users keep coming back to it every single week.</p>
</article>

<div class="abs contact-photo" role="img" aria-label="Green tinted photo of palm leaves"></div>
<h2 class="abs contact-title">Interested? Leave Email Here.</h2>
<label class="check" style="left:96px"><svg width="14" height="12" viewBox="0 0 14 12"><path d="M1 6l4 4 8-9" fill="none" stroke="#3bb54a" stroke-width="2.5"/></svg><span>Business<br>Owner</span></label>
<label class="check" style="left:229px"><span class="box"></span><span>App<br>Owner</span></label>
<div class="abs field">Your email here...</div>
<a class="abs send">Leave a Message</a>

<footer>
  <div class="abs footer"></div>
  <div class="abs footer-green"></div>
  <div class="abs footer-brand">KLORVIN</div>
  <nav class="footer-nav">
    <a style="left:648px">What is Klorvin?</a>
    <a style="left:756px">Why Norvale?</a>
    <a style="left:856px">How it Works</a>
    <a style="left:960px">Get Access</a>
  </nav>
</footer>

</body>
</html>
```